TIVRO

We provide order application for restaurants.
We need something modern, with a real visual identity.
it must be a landscape format.
Here our website: www.tivro.agency
a mix between those two leaflet would be great:
https://quelmart.brivodesk.com/share/ZtRwMnPq8L2x7bVyHc3d9/1
(landscape format)
https://app.nortelio.com/documents/4172906/view/518246097?accessId=3fa91d

IMPORTANT: this is not for taking. it's a leaflet to share by mail. (7 - 8 pages max)

Industry/Entity Type

web developement

Colors
6B429C
8869AF
B7A5CE
E3DAEB
F3F0F8

Requirements
Must have
• landscape format, to send by email (not for print).

```html
<!DOCTYPE html>
<html lang="fr">
<head>
<meta charset="utf-8">
<title>TIVRO – Dépliant application restaurant</title>
<link href="https://fonts.googleapis.com/css2?family=Poppins:wght@300;400;500;600;700;800;900&display=swap" rel="stylesheet">
<style>
:root{
  --navy:#2b1590;
  --deep:#5a22e4;
  --violet:#7b34ee;
  --orchid:#a24af2;
  --lilac:#c9a8f5;
  --mist:#f3f0f8;
  --ink:#1b1b1f;
  --charcoal:#262528;
  --white:#ffffff;
  --title:#6a26e6;
}
*{margin:0;padding:0;box-sizing:border-box}
html,body{width:1200px;height:2362px;overflow:hidden}
body{background:var(--navy);font-family:'Poppins',sans-serif;color:var(--ink);position:relative}
.spread{position:absolute;left:60px;width:1080px;height:764px;display:flex;box-shadow:0 20px 50px rgba(0,0,0,.25)}
.spread--outer{top:358px}
.spread--inner{top:1242px}
.panel{position:relative;width:360px;height:764px;overflow:hidden;background:var(--white)}
.abs{position:absolute}
.deco{position:absolute;left:0;top:0;width:100%;height:100%}
.placeholder{position:absolute;border-radius:6px}

/* panel: why */
.why__title{left:44px;top:40px;font-size:30px;line-height:32px;font-weight:800;color:var(--title);letter-spacing:.2px}
.why__sub{left:44px;top:176px;font-size:15px;font-weight:700;color:var(--orchid)}
.why__body{left:44px;top:206px;width:272px;font-size:12.6px;line-height:18px;color:var(--ink)}

/* panel: coaching */
.coach{left:42px;top:42px;width:272px;height:680px;background:linear-gradient(170deg,#8a3ff0 0%,#6a2ef0 55%,#4a12f0 100%)}
.coach__title{left:24px;top:22px;font-size:33px;line-height:34px;font-weight:900;color:var(--white)}
.coach__body{left:24px;top:100px;width:236px;font-size:12.8px;line-height:18px;color:var(--white)}
.coach__touch{left:32px;top:468px;font-size:18px;font-weight:700;color:var(--white)}
.coach__label{font-size:13.5px;color:#c6a8ff;left:34px}
.coach__value{font-size:13.5px;color:var(--white);font-weight:500;left:34px}

/* panel: cover */
.phone{position:absolute;border:7px solid #1e1e22;border-radius:34px;background:var(--white);box-shadow:0 10px 25px rgba(40,20,90,.25)}
.brand{display:flex;align-items:center;gap:10px;font-size:30px;font-weight:600;color:var(--deep);letter-spacing:1px}
.brand__mark{width:24px;height:24px;background:var(--deep)}
.search{border:2px solid #cdbff0;border-radius:22px;height:42px;display:flex;align-items:center;justify-content:space-between;padding:0 3px 0 18px;font-size:12.5px;color:#444}
.search__btn{width:34px;height:34px;border-radius:50%;background:var(--deep);display:flex;align-items:center;justify-content:center}
.cover__title{left:0;width:360px;text-align:center;top:500px;font-size:46px;line-height:46px;font-weight:900;color:var(--white)}
.cover__sub{left:0;width:360px;text-align:center;top:600px;font-size:21px;font-weight:800;color:var(--ink)}
.cover__body{left:0;width:360px;text-align:center;top:640px;font-size:19px;line-height:23px;color:#f1e6ff;font-weight:300}

/* panel: control */
.iconcircle{position:absolute;width:86px;height:86px;border-radius:50%;display:flex;align-items:center;justify-content:center;box-shadow:0 6px 12px rgba(40,10,110,.35)}
.iconlabel{position:absolute;font-size:9.5px;font-weight:700;color:var(--white);text-align:center;width:110px;white-space:nowrap}
.control__title{left:42px;top:522px;font-size:27px;line-height:32px;font-weight:700;color:var(--title)}
.control__body{left:42px;top:594px;width:280px;font-size:12.4px;line-height:18.4px}

/* panel: simple */
.simple{background:var(--charcoal)}
.simple__title{left:42px;top:162px;font-size:29px;line-height:32px;font-weight:600;color:#8a5cf3}
.feature{position:absolute;left:42px;width:300px}
.feature__hex{position:absolute;left:0;top:0}
.feature__name{position:absolute;left:80px;top:-6px;font-size:23px;line-height:24px;color:var(--white);font-weight:400;width:220px}
.feature__rule{position:absolute;left:80px;width:32px;height:2px;background:var(--violet)}
.feature__text{position:absolute;left:80px;width:200px;font-size:11.5px;line-height:17.5px;color:#eee}

/* panel: features */
.disc__title{left:26px;top:28px;font-size:30px;line-height:31px;font-weight:700;color:var(--ink)}
.fblock{position:absolute;color:var(--white)}
.fblock__name{font-size:16px;font-weight:400;line-height:19px}
.fblock__text{font-size:8px;line-height:10px;margin-top:3px;color:#f0e6ff}
</style>
</head>
<body>

<section class="spread spread--outer">

  <article class="panel panel--why">
    <svg class="deco" viewBox="0 0 360 764" aria-hidden="true">
      <defs>
        <linearGradient id="gWhy" x1="0" y1="0" x2="1" y2="1"><stop offset="0" stop-color="#9b45f2"/><stop offset="1" stop-color="#5a24e8"/></linearGradient>
      </defs>
      <polygon points="232,0 360,0 360,72" fill="#6a30ec"/>
      <polygon points="290,0 360,0 360,40" fill="#9a4cf2"/>
      <polygon points="0,520 360,490 360,764 0,764" fill="url(#gWhy)"/>
      <polygon points="0,560 200,764 0,764" fill="#b25cf5" opacity=".55"/>
    </svg>
    <h1 class="abs why__title">POURQUOI UNE<br>APP POUR<br>VOTRE<br>RESTAURANT ?</h1>
    <p class="abs why__sub">UN CHIFFRE D'AFFAIRE DOUBLÉ !</p>
    <p class="abs why__body">Grâce à un taux de conversion client 3 fois supérieur au web, l'application mobile permet à nos restaurateurs partenaires de multiplier les commandes et d'augmenter la valeur du panier moyen. Votre application personnelle, la vitrine idéale pour booster votre activité !</p>
    <div class="placeholder" role="img" aria-label="Deux smartphones affichant le menu de commande d'un restaurant" style="left:48px;top:360px;width:270px;height:240px;background:linear-gradient(160deg,#f4f4f6 0%,#d9d6df 60%,#8c7f88 100%);border-radius:22px"></div>
  </article>

  <article class="panel panel--coach">
    <div class="abs coach">
      <h2 class="abs coach__title">COACHING<br>DIGITAL</h2>
      <p class="abs coach__body">Pour donner à votre application une visibilité maximale, notre équipe est à vos côtés pour développer et guider votre stratégie digitale. Opérations promotionnelles, programmes de fidélité, communication sur les réseaux sociaux et publicité (Print et Web) sont autant de leviers d'actions pour vous mener au succès.</p>
      <div class="placeholder" role="img" aria-label="Smartphone incliné affichant un fil de réseau social" style="left:58px;top:290px;width:150px;height:140px;background:radial-gradient(circle,#f0e8ff 0%,#c6a6f8 55%,rgba(160,110,245,0) 75%)"></div>
      <p class="abs coach__touch">GET IN TOUCH</p>
      <p class="abs coach__label" style="top:508px">Phone</p>
      <p class="abs coach__value" style="top:524px">06 40 17 52 88</p>
      <p class="abs coach__label" style="top:550px">Email</p>
      <p class="abs coach__value" style="top:566px">contact@tivro.agency</p>
      <p class="abs coach__label" style="top:592px">Web</p>
      <p class="abs coach__value" style="top:608px">www.tivro.agency</p>
    </div>
  </article>

  <article class="panel panel--cover" style="background:linear-gradient(180deg,#f6f2fb,#ece4f6)">
    <svg class="deco" viewBox="0 0 360 764" aria-hidden="true">
      <defs>
        <linearGradient id="gCover" x1="0" y1="0" x2="0" y2="1"><stop offset="0" stop-color="#7f3cf0"/><stop offset="1" stop-color="#a64ef4"/></linearGradient>
      </defs>
      <polygon points="0,0 90,0 0,110" fill="#7a3cee"/>
      <polygon points="0,0 40,0 0,60" fill="#a457f3"/>
    </svg>
    <div class="phone" style="left:62px;top:88px;width:238px;height:430px">
      <div class="abs brand" style="left:34px;top:100px"><span class="brand__mark"></span>TIVRO</div>
      <div class="abs search" style="left:12px;top:186px;width:200px"><span>Poulet Doré</span><span class="search__btn"><svg width="16" height="16" viewBox="0 0 16 16"><circle cx="7" cy="7" r="5" fill="none" stroke="#fff" stroke-width="1.8"/><line x1="11" y1="11" x2="15" y2="15" stroke="#fff" stroke-width="1.8"/></svg></span></div>
    </div>
    <svg class="deco" viewBox="0 0 360 764" aria-hidden="true">
      <polygon points="0,508 360,300 360,764 0,764" fill="url(#gCover)"/>
      <polygon points="0,508 360,390 360,430 0,560" fill="#6a2ee8" opacity=".45"/>
    </svg>
    <h2 class="abs cover__title">ENSEMBLE<br>CREEONS</h2>
    <p class="abs cover__sub">VOTRE APPLICATION</p>
    <p class="abs cover__body">vos clients recherchent<br>votre application sur<br>leur boutique d'applications</p>
  </article>
</section>

<section class="spread spread--inner">

  <article class="panel panel--control">
    <svg class="deco" viewBox="0 0 360 764" aria-hidden="true">
      <defs>
        <linearGradient id="gCtrl" x1="0" y1="0" x2="1" y2="1"><stop offset="0" stop-color="#6430ec"/><stop offset="1" stop-color="#9a48f2"/></linearGradient>
      </defs>
      <polygon points="0,0 360,0 360,470 0,380" fill="url(#gCtrl)"/>
      <polygon points="0,100 360,130 360,210 0,140" fill="#4f20e0" opacity=".35"/>
      <polygon points="0,380 360,470 0,500" fill="#ffffff"/>
    </svg>
    <div class="iconcircle" style="left:32px;top:30px;background:#7d48ee"><svg width="44" height="40" viewBox="0 0 44 40"><rect x="3" y="3" width="38" height="26" rx="2" fill="none" stroke="#fff" stroke-width="3"/><polygon points="18,10 28,16 18,22" fill="#fff"/><rect x="18" y="29" width="8" height="6" fill="#fff"/><rect x="12" y="35" width="20" height="3" fill="#fff"/></svg></div>
    <div class="iconcircle" style="left:134px;top:30px;background:#a95cf2"><svg width="36" height="44" viewBox="0 0 36 44"><path d="M13 4a3 3 0 0 1 6 0v16l4-1a3 3 0 0 1 3 0l4 1a3 3 0 0 1 3 3v10c0 6-5 10-11 10h-3c-4 0-7-2-9-5L4 27a3 3 0 0 1 5-4l4 4z" fill="#fff"/></svg></div>
    <div class="iconcircle" style="left:236px;top:30px;background:#7d48ee"><svg width="28" height="44" viewBox="0 0 28 44"><rect x="3" y="2" width="22" height="40" rx="4" fill="none" stroke="#fff" stroke-width="3"/><rect x="7" y="7" width="14" height="26" fill="#fff"/><circle cx="14" cy="37" r="2" fill="#fff"/></svg></div>
    <p class="iconlabel" style="left:20px;top:126px">FORMATION</p>
    <p class="iconlabel" style="left:122px;top:126px">ADMIN PANEL</p>
    <p class="iconlabel" style="left:224px;top:126px">APPLICATION MOBILE</p>
    <div class="phone" style="left:60px;top:160px;width:150px;height:306px;background:#1e1e22;border-radius:22px">
      <div class="placeholder" role="img" aria-label="Écran d'accueil d'une application de restaurant avec un seau de poulet frit" style="left:3px;top:3px;right:3px;bottom:3px;background:linear-gradient(180deg,#1b1b1b 0%,#3a2616 35%,#e07a2a 52%,#c9161d 80%,#111 100%);border-radius:16px"></div>
    </div>
    <div class="phone" style="left:222px;top:304px;width:80px;height:160px;background:#1e1e22;border-radius:14px;border-width:4px">
      <div class="placeholder" role="img" aria-label="Écran de menu de l'application avec liste de plats" style="left:2px;top:2px;right:2px;bottom:2px;background:linear-gradient(180deg,#222 0%,#f07b1e 25%,#fafafa 40%,#eee 100%);border-radius:10px"></div>
    </div>
    <h2 class="abs control__title">VOTRE APPLICATION<br>TOUT EN CONTRÔLE</h2>
    <p class="abs control__body">Via une tablette ou un smartphone avec une application dédiée, vous exploitez pleinement le potentiel de votre application. Vous pourrez alors : Gérer vos commandes, gérer vos produits, envoyer une notification personnalisée, définir des zones de livraison.</p>
  </article>

  <article class="panel simple">
    <div class="placeholder" role="img" aria-label="Faisceaux lumineux abstraits bleus et violets" style="left:80px;top:0;width:200px;height:150px;border-radius:0;background:linear-gradient(180deg,#3a2aa8 0%,#5a3fe0 35%,rgba(38,37,40,0) 100%)"></div>
    <h2 class="abs simple__title">LA SIMPLICITÉ<br>À VOTRE PORTÉE</h2>

    <div class="feature" style="top:250px">
      <svg class="feature__hex" width="50" height="56" viewBox="0 0 50 56"><polygon points="25,1 49,14 49,42 25,55 1,42 1,14" fill="#7b3ff0"/><path d="M14 28l22-10-8 22-4-8z" fill="none" stroke="#fff" stroke-width="2"/></svg>
      <p class="feature__name">Ma propre<br>application</p>
      <span class="feature__rule" style="top:52px"></span>
      <p class="feature__text" style="top:66px">Je m'équipe d'une application sur mesure. Votre logo, votre menu, votre restaurant!</p>
    </div>
    <div class="feature" style="top:430px">
      <svg class="feature__hex" width="50" height="56" viewBox="0 0 50 56"><polygon points="25,1 49,14 49,42 25,55 1,42 1,14" fill="#7b3ff0"/><path d="M13 24h6l12-7v22l-12-7h-6z" fill="none" stroke="#fff" stroke-width="2"/></svg>
      <p class="feature__name">Mon chiffre<br>d'affaires boosté</p>
      <span class="feature__rule" style="top:52px"></span>
      <p class="feature__text" style="top:66px">Mes commandes décollent grâce à un outil performant.</p>
    </div>
    <div class="feature" style="top:588px">
      <svg class="feature__hex" width="50" height="56" viewBox="0 0 50 56"><polygon points="25,1 49,14 49,42 25,55 1,42 1,14" fill="#7b3ff0"/><circle cx="25" cy="25" r="7" fill="none" stroke="#fff" stroke-width="2"/><rect x="21" y="33" width="8" height="6" fill="#fff"/></svg>
      <p class="feature__name">Mon coach<br>marketing</p>
      <span class="feature__rule" style="top:52px"></span>
      <p class="feature__text" style="top:66px">Nos experts sont à vos côtés pour optimiser votre communication digitale.</p>
    </div>
  </article>

  <article class="panel panel--features">
    <svg class="deco" viewBox="0 0 360 764" aria-hidden="true">
      <defs>
        <linearGradient id="gFeat" x1="0" y1="0" x2="1" y2="1"><stop offset="0" stop-color="#6a34ec"/><stop offset="1" stop-color="#9c4af2"/></linearGradient>
      </defs>
      <polygon points="0,270 360,330 360,764 0,764" fill="url(#gFeat)"/>
      <rect x="0" y="320" width="170" height="84" fill="#8a48f0" opacity=".7"/>
      <rect x="0" y="408" width="360" height="88" fill="#7a40ee" opacity=".6"/>
      <rect x="0" y="500" width="360" height="66" fill="#6a34ec" opacity=".55"/>
      <rect x="180" y="540" width="180" height="64" fill="#8a4ef2" opacity=".5"/>
    </svg>
    <h2 class="abs disc__title">DÉCOUVREZ VOS<br>FONCTIONNALITÉS</h2>
    <div class="placeholder" role="img" aria-label="Illustration d'un point d'interrogation dans un disque violet" style="left:22px;top:124px;width:120px;height:120px;border-radius:50%;background:radial-gradient(circle at 40% 40%,#efe6ff,#c5a4f6 70%)"></div>
    <div class="phone" style="left:186px;top:104px;width:140px;height:282px;border-width:4px;border-color:#d8d8dc;border-radius:20px">
      <div class="placeholder" role="img" aria-label="Écran de l'application montrant un plateau de sushis" style="left:4px;top:28px;right:4px;bottom:30px;background:linear-gradient(160deg,#2b2b2b 0%,#e2e0dc 40%,#d8525a 60%,#1c1c1c 100%);border-radius:4px"></div>
    </div>
    <div class="fblock" style="left:20px;top:330px;width:150px"><p class="fblock__name">UNE LIVRAISON<br>MAITRISÉE</p><p class="fblock__text">Définissez un montant de commande minimum par secteur.</p></div>
    <div class="fblock" style="left:22px;top:424px;width:140px"><p class="fblock__name">STATISTIQUES</p><p class="fblock__text">Définissez un montant de commande minimum par secteur.</p></div>
    <div class="fblock" style="left:198px;top:420px;width:150px"><p class="fblock__name">FACILITEZ L'ACHAT</p><p class="fblock__text">Un processus de commande simplifié grâce aux moyens de paiements enregistrés.</p></div>
    <div class="fblock" style="left:22px;top:508px;width:150px"><p class="fblock__name">DÉMARQUEZ-VOUS</p><p class="fblock__text">Distancez vos concurrents grâce à un outil numérique innovant.</p></div>
    <div class="fblock" style="left:200px;top:546px;width:150px"><p class="fblock__name">CLICK &amp; COLLECT</p><p class="fblock__text">Vos clients choisissent la livraison ou le Click &amp; Collect.</p></div>
    <div class="iconcircle" style="left:28px;top:616px;width:82px;height:82px;background:#7d48ee"><svg width="38" height="38" viewBox="0 0 38 38"><polygon points="8,4 32,19 8,34" fill="none" stroke="#fff" stroke-width="3"/><polygon points="13,12 24,19 13,26" fill="#fff"/></svg></div>
    <div class="iconcircle" style="left:140px;top:616px;width:82px;height:82px;background:#a95cf2"><svg width="40" height="36" viewBox="0 0 40 36"><path d="M4 12h8l20-10v30L12 22H4z" fill="#fff"/><rect x="10" y="22" width="6" height="12" fill="#fff"/></svg></div>
    <div class="iconcircle" style="left:252px;top:616px;width:82px;height:82px;background:#7d48ee"><svg width="36" height="36" viewBox="0 0 36 36" fill="none" stroke="#fff" stroke-width="3"><rect x="3" y="3" width="11" height="11"/><rect x="22" y="3" width="11" height="11"/><rect x="3" y="22" width="11" height="11"/><path d="M22 22h5v5h6M22 30v3h4"/></svg></div>
    <p class="iconlabel" style="left:14px;top:712px;color:var(--ink)">STICKERS</p>
    <p class="iconlabel" style="left:126px;top:712px;color:var(--ink)">DIGITAL MARKETING</p>
    <p class="iconlabel" style="left:238px;top:712px;color:var(--ink)">FLYER</p>
  </article>
</section>

</body>
</html>
```